Cell phone repair

you can please design me business card

size 3.5" x 2"

colors blue and red

fixit rapid logo (you get from my website fixitrapidco.example )

"We Come To You!

It is very simple! You tell us what phone you have, And we come to fix it."

phone number: 555.248.3906

website: www.fixitrapidco.example

email: info@fixitrapidco.example

```html
<!DOCTYPE html>
<html lang="en">
<head>
<meta charset="utf-8">
<title>Fixit Rapid – Business Card</title>
<link rel="stylesheet" href="https://fonts.googleapis.com/css2?family=Open+Sans:wght@400;600;700&display=swap">
<style>
  :root {
    --sky: #29a8e0;
    --sky-deep: #1f93c9;
    --signal-red: #e5202a;
    --paper: #ffffff;
    --ink: #1c1c1c;
    --backdrop: #d9dadc;
  }
  * { margin: 0; padding: 0; box-sizing: border-box; }
  html, body { width: 1200px; height: 977px; overflow: hidden; }
  body {
    background: var(--backdrop);
    font-family: "Open Sans", Arial, sans-serif;
    position: relative;
  }
  .card {
    position: absolute;
    width: 560px;
    height: 320px;
    overflow: hidden;
    box-shadow: 0 6px 18px rgba(0,0,0,0.18);
  }

  /* Back side */
  .card-back {
    left: 60px; top: 110px;
    background: var(--sky);
    color: var(--paper);
  }
  .back-brand {
    position: absolute;
    left: 0; right: 0; top: 98px;
    display: flex; align-items: center; justify-content: center; gap: 14px;
  }
  .brand-dot {
    width: 22px; height: 22px; border-radius: 50%;
    background: var(--paper);
  }
  .back-brand .brand-name {
    font-size: 40px; font-weight: 700; letter-spacing: -0.5px;
    color: var(--paper);
  }
  .tagline {
    position: absolute;
    left: 0; right: 0; top: 200px;
    text-align: center;
    font-size: 16px; font-weight: 700; line-height: 1.45;
  }

  /* Front side */
  .card-front {
    left: 580px; top: 480px;
    background: var(--paper);
  }
  .front-brand {
    position: absolute; left: 34px; top: 96px;
    display: flex; align-items: center; gap: 10px;
  }
  .front-brand .brand-dot { background: var(--signal-red); width: 18px; height: 18px; }
  .front-brand .brand-name {
    font-size: 30px; font-weight: 700; color: var(--sky); letter-spacing: -0.5px;
  }
  .person {
    position: absolute; right: 40px; top: 40px; text-align: right;
  }
  .person-name { font-size: 16px; font-weight: 700; color: var(--signal-red); }
  .person-role { font-size: 10px; font-weight: 600; color: var(--ink); }
  .edge-tab {
    position: absolute; right: 0; top: 36px;
    width: 18px; height: 48px; background: var(--sky);
  }
  .wave { position: absolute; left: 0; top: 0; }
  .contact {
    position: absolute; right: 24px; top: 232px;
    list-style: none; color: var(--paper);
    font-size: 11.5px; line-height: 1.6;
  }
  .contact li { display: flex; align-items: center; gap: 8px; }
  .contact svg { width: 11px; height: 11px; fill: var(--paper); flex: none; }
  .address {
    position: absolute; left: 40px; top: 262px;
    color: var(--paper); font-size: 13px; line-height: 1.5;
  }
</style>
</head>
<body>

<section class="card card-back" aria-label="Business card back">
  <div class="back-brand">
    <span class="brand-dot"></span>
    <span class="brand-name">Fixit Rapid</span>
  </div>
  <p class="tagline">
    We Come To You! It is very simple!<br>
    You tell us what phone you have, And we come to fix it.
  </p>
</section>

<section class="card card-front" aria-label="Business card front">
  <svg class="wave" width="560" height="320" viewBox="0 0 560 320" aria-hidden="true">
    <path d="M0,196 C120,262 250,246 360,206 S500,142 560,138 L560,320 L0,320 Z" fill="var(--sky)"/>
    <path d="M0,176 C120,242 250,226 360,186 S500,122 560,118" fill="none" stroke="var(--signal-red)" stroke-width="7"/>
  </svg>

  <div class="edge-tab"></div>

  <div class="person">
    <p class="person-name">Dana Whitfield</p>
    <p class="person-role">President</p>
  </div>

  <div class="front-brand">
    <span class="brand-name">Fixit Rapid</span>
    <span class="brand-dot"></span>
  </div>

  <ul class="contact">
    <li>
      <svg viewBox="0 0 24 24"><path d="M6.6 10.8a15 15 0 0 0 6.6 6.6l2.2-2.2a1 1 0 0 1 1-.25 11.4 11.4 0 0 0 3.6.57 1 1 0 0 1 1 1V20a1 1 0 0 1-1 1A17 17 0 0 1 3 4a1 1 0 0 1 1-1h3.5a1 1 0 0 1 1 1c0 1.25.2 2.45.57 3.57a1 1 0 0 1-.25 1z"/></svg>
      555.248.3906
    </li>
    <li>
      <svg viewBox="0 0 24 24"><path d="M2 5h20v14H2z M2 5l10 7 10-7" fill="none" stroke="#fff" stroke-width="2.4"/></svg>
      info@fixitrapidco.example
    </li>
    <li>
      <svg viewBox="0 0 24 24"><circle cx="12" cy="12" r="9.5" fill="none" stroke="#fff" stroke-width="2.4"/><path d="M2.5 12h19M12 2.5c3 3 3 16 0 19M12 2.5c-3 3-3 16 0 19" fill="none" stroke="#fff" stroke-width="1.8"/></svg>
      www.fixitrapidco.example
    </li>
  </ul>

  <p class="address">418 Alder Grove Ln,<br>Millbrook, PA 18920</p>
</section>

</body>
</html>
```